Grupo VZ FaceBook - Avatar and Cover

We currently have our own logo, but it doesn't fit the circular shape in the Facebook avatar section, so we need a creative designer that using the same logo can make it look good in the FB avatar section, also we need a modern and minimalist facebook cover, you can get inspiration from our website grupovz-example.com

In the banner you can add the logo, but in small, computer reference, techonolgy datacenter images would be a good background.

Industry/Entity Type

Technology Equipment

Logo Text

Grupo VZ

Requirements
Must have
• Modern, Minimalist

```html
<!DOCTYPE html>
<html lang="es">
<head>
<meta charset="utf-8">
<title>Grupo VZ – Portada de Facebook</title>
<link rel="stylesheet" href="https://fonts.googleapis.com/css2?family=Bebas+Neue&display=swap">
<style>
  :root {
    --canvas-bg: #f2f2f2;
    --headline: #ffffff;
    --headline-shadow: rgba(0, 0, 0, 0.85);
    --badge-bg: #ffffff;
    --badge-ring: #4a5a62;
    --brand: #3f6f7c;
    --photo-dark: #1b2a30;
    --photo-mid: #5f7e88;
    --photo-light: #dfe8ec;
  }
  * { margin: 0; padding: 0; box-sizing: border-box; }
  html, body {
    width: 1200px;
    height: 960px;
    overflow: hidden;
    background: var(--canvas-bg);
  }
  .canvas {
    position: relative;
    width: 1200px;
    height: 960px;
    background: var(--canvas-bg);
  }
  .cover {
    position: absolute;
    left: 46px;
    top: 206px;
    width: 1108px;
    height: 411px;
    overflow: hidden;
  }
  .cover-photo {
    position: absolute;
    inset: 0;
    background:
      radial-gradient(ellipse 30% 60% at 72% 50%, rgba(255,255,255,0.55), transparent 70%),
      linear-gradient(90deg, var(--photo-dark) 0%, #2c4047 25%, var(--photo-mid) 50%, var(--photo-light) 70%, #b9c7cd 100%);
  }
  .headline {
    position: absolute;
    left: 702px;
    top: 0;
    font-family: "Bebas Neue", "Arial Narrow", sans-serif;
    font-weight: 400;
    color: var(--headline);
    text-transform: uppercase;
    text-shadow: 3px 3px 3px var(--headline-shadow);
  }
  .headline span {
    position: absolute;
    left: 0;
    white-space: nowrap;
    line-height: 1;
  }
  .line-lead    { top: 38px;  font-size: 64px; letter-spacing: 1px; }
  .line-big-1   { top: 99px;  font-size: 88px; }
  .line-small-1 { top: 181px; font-size: 48px; }
  .line-big-2   { top: 233px; font-size: 91px; }
  .line-small-2 { top: 324px; font-size: 43px; }

  .avatar {
    position: absolute;
    left: 106px;
    top: 520px;
    width: 233px;
    height: 233px;
    border-radius: 50%;
    background: var(--badge-bg);
    border: 4px solid var(--badge-ring);
    display: flex;
    align-items: center;
    justify-content: center;
  }
  .avatar-name {
    font-family: "Bebas Neue", "Arial Narrow", sans-serif;
    font-weight: 400;
    font-size: 52px;
    color: var(--brand);
  }
</style>
</head>
<body>
  <main class="canvas">
    <section class="cover">
      <div class="cover-photo" role="img" aria-label="Pasillo de centro de datos con racks de servidores y luces de red"></div>
      <h1 class="headline">
        <span class="line-lead">Brindamos</span>
        <span class="line-big-1">Soluciones</span>
        <span class="line-small-1">a todos sus</span>
        <span class="line-big-2">Problemas</span>
        <span class="line-small-2">de tecnología</span>
      </h1>
    </section>
    <div class="avatar">
      <span class="avatar-name">Grupo VZ</span>
    </div>
  </main>
</body>
</html>
```